Refer a Friend A5 Flyer for Healthcare Staff

We need an A5 flyer that we can hand out to existing and new staff members promoting our Refer a friend Scheme. We need the leaflet to encourage staff to talk to their family and friends about joining our Healthcare Agency, which provides staff to local care related establishments. Using our logo and brand colours blue and green, as per our website, the final design will need to clearly convey the benefits and attractions of referring additional staff to the team. In addition is the promotion of our Circlesphere page, requesting staff to like the page and to like and share various posts.

Target Market(s)

Healthcare and potential Healthcare Staff

Industry/Entity Type

Healthcare

Colors
33b8a4
3277b5

Requirements
Must have
• Company Logo, Brand colours,
• text; "Refer a Friend and receive a £50 Bonus after just 1 completed shift"
• text; "3 easy steps to refer a friend, 1 Fill out your name on the back of your Business Card 2 Hand the card to your friend or any person you wish to refer, 3 ask your friend to present the card to us when they attend their interview"
• text; "Like and share any of our Open Days on Circlesphere for a chance to win a prize, you can find us easily by searching @CarewellPlacementGroup"
• text; "Like our Page to stay up to date with our events and offers"
Nice to have
• care worker / elderly care / support worker pictures
• Content / pics from website www.carewellplacementgroup.co.uk

```html
<!DOCTYPE html>
<html lang="en">
<head>
<meta charset="utf-8">
<title>Refer a Friend – A5 Flyer</title>
<link href="https://fonts.googleapis.com/css2?family=Oswald:wght@300;400;500;600&display=swap" rel="stylesheet">
<style>
  :root {
    --brand-blue: #3d82d6;
    --stripe-blue: #2f6ee0;
    --brand-green: #4ef590;
    --step-blue: #4aa5f2;
    --step-green: #4ff08e;
    --pill-blue: #3f86e0;
    --white: #ffffff;
    --ink-blue: #2a5fd0;
    --page-bg: #eef1f4;
  }
  * { margin: 0; padding: 0; box-sizing: border-box; }
  html, body {
    width: 1200px; height: 1200px; overflow: hidden;
    background: var(--page-bg);
    font-family: "Oswald", "Arial Narrow", sans-serif;
  }
  .canvas { position: relative; width: 1200px; height: 1200px; overflow: hidden; }
  .flyer {
    position: absolute; left: 207px; top: 20px;
    width: 988px; height: 1458px;
    transform: scale(0.7956); transform-origin: top left;
    background: var(--white);
    overflow: hidden;
    box-shadow: 0 10px 40px rgba(0,0,0,0.18);
  }
  .flyer-art { position: absolute; inset: 0; width: 988px; height: 1458px; }

  .headline {
    position: absolute; left: 63px; top: 68px;
    color: var(--white); font-weight: 600; font-size: 131px;
    line-height: 1; letter-spacing: -5px; white-space: nowrap;
  }
  .headline-rule {
    position: absolute; left: 68px; top: 226px;
    width: 163px; height: 10px; background: var(--white);
  }
  .offer {
    position: absolute; left: 66px; top: 256px;
    color: var(--white); font-weight: 300; font-size: 77px;
    line-height: 75px; letter-spacing: -1px;
  }

  .steps-title {
    position: absolute; left: 70px; top: 728px;
    width: 538px; height: 62px;
    background: var(--pill-blue);
    border-radius: 0 31px 31px 0;
    color: var(--white); font-weight: 400; font-size: 38px;
    line-height: 62px; padding-left: 40px;
    box-shadow: 0 3px 8px rgba(0,0,0,0.2);
  }
  .steps-title strong { font-weight: 600; font-size: 46px; }
  .steps { position: absolute; left: 70px; top: 810px; width: 531px; list-style: none; }
  .step {
    display: flex; height: 98px; margin-bottom: 9px;
    background: linear-gradient(90deg, var(--step-blue), var(--step-green));
    box-shadow: 0 3px 8px rgba(0,0,0,0.2);
  }
  .step-number {
    width: 93px; flex: none;
    background: var(--step-blue);
    border: 2px solid rgba(255,255,255,0.5);
    color: var(--white); font-weight: 500; font-size: 66px;
    display: flex; align-items: center; justify-content: center;
  }
  .step-text {
    color: var(--white); font-weight: 400; font-size: 27px;
    line-height: 30px; padding: 0 8px 0 24px;
    display: flex; align-items: center;
  }

  .brand {
    position: absolute; left: 73px; top: 1318px;
    display: flex; align-items: center; gap: 10px;
  }
  .brand-dot { width: 30px; height: 30px; border-radius: 50%; background: var(--ink-blue); }
  .brand-name { color: var(--ink-blue); font-weight: 400; font-size: 28px; line-height: 1; }

  .social-ring {
    position: absolute; left: 836px; top: 1190px;
    width: 80px; height: 80px; border-radius: 50%;
    border: 4px solid var(--ink-blue);
  }
  .social {
    position: absolute; right: 72px; top: 1278px; width: 520px;
    text-align: right; color: var(--white);
  }
  .social-handle { font-weight: 400; font-size: 30px; line-height: 40px; }
  .social-note { font-weight: 300; font-size: 19px; line-height: 21px; margin-top: 12px; }
  .social-note + .social-note { margin-top: 10px; }
</style>
</head>
<body>
<main class="canvas">
  <article class="flyer">
    <svg class="flyer-art" viewBox="0 0 988 1458" xmlns="http://www.w3.org/2000/svg">
      <defs>
        <linearGradient id="careScene" x1="0" y1="0" x2="1" y2="1">
          <stop offset="0" stop-color="#b8d8f0"/>
          <stop offset="0.45" stop-color="#d9ecf4"/>
          <stop offset="0.75" stop-color="#9fd88a"/>
          <stop offset="1" stop-color="#c8e6d8"/>
        </linearGradient>
        <linearGradient id="gardenTint" x1="0" y1="0" x2="1" y2="1">
          <stop offset="0" stop-color="#3b7fd3"/>
          <stop offset="0.6" stop-color="#4387d9"/>
          <stop offset="1" stop-color="#3a7cd0"/>
        </linearGradient>
      </defs>

      <g role="img" aria-label="Photo: smiling care worker leaning towards an elderly woman seated outdoors">
        <rect x="0" y="0" width="988" height="1246" fill="url(#careScene)"/>
      </g>

      <path d="M0 658 C490 648 870 470 988 290 L988 0 L0 0 Z" fill="var(--brand-green)"/>
      <path d="M0 650 C480 640 860 450 988 240 L988 0 L0 0 Z" fill="var(--stripe-blue)"/>
      <path d="M0 640 C470 630 850 420 988 160 L988 0 L0 0 Z" fill="var(--white)"/>
      <g role="img" aria-label="Blue-tinted photo: care worker walking with an elderly man in a garden">
        <path d="M0 610 C450 600 820 380 988 0 L0 0 Z" fill="url(#gardenTint)"/>
      </g>

      <rect x="0" y="1246" width="988" height="212" fill="var(--white)"/>
      <path d="M270 1458 C480 1200 700 1070 988 1050 V1458 Z" fill="var(--brand-green)"/>
      <path d="M290 1458 C500 1215 720 1100 988 1100 V1458 Z" fill="var(--stripe-blue)"/>
      <path d="M310 1458 C520 1230 740 1130 988 1132 V1458 Z" fill="var(--white)"/>
      <path d="M345 1458 C550 1250 760 1165 988 1165 V1458 Z" fill="var(--brand-green)"/>
    </svg>

    <h1 class="headline">Refer a Friend</h1>
    <div class="headline-rule"></div>
    <p class="offer">and receive a £50<br>Bonus after just 1<br>completed shift</p>

    <h2 class="steps-title"><strong>3</strong> EASY STEPS TO REFER A FRIEND</h2>
    <ol class="steps">
      <li class="step"><span class="step-number">1</span><span class="step-text">Fill out your name on the back of your<br>Business Card</span></li>
      <li class="step"><span class="step-number">2</span><span class="step-text">Hand the card to your friend or any<br>person you wish to refer</span></li>
      <li class="step"><span class="step-number">3</span><span class="step-text">Ask your friend to present the card to<br>us when they attend their interview</span></li>
    </ol>

    <div class="brand">
      <span class="brand-dot"></span>
      <span class="brand-name">Carewell Placement</span>
    </div>

    <div class="social-ring"></div>
    <div class="social">
      <p class="social-handle">@CarewellPlacementGroup</p>
      <p class="social-note">Like and share any of our Open Days on Circlesphere for a<br>chance to win a prize.</p>
      <p class="social-note">Like our Page to stay up to date with our events and offers</p>
    </div>
  </article>
</main>
</body>
</html>
```